Website for 3d printing & other services

Hi, i'm after a website to sell my 3d printed automotive parts as well as sell my 3d printing services & other services.

There's a few things i need the website to have:

- Automatic 3d print quoting based on the file the client uploads to the website.
- Shop function where i can sell my custom automotive parts
- 3D printing technologies offered are SLA & FDM
- My business can offer 3d printing, 3d scanning, 3d cad design, cnc machining, steel fabrication, drafting services.

The color design is to suit my logo which is Black, orange & white.

Target Market(s)

3d printing, automotive, fabrication

Industry/Entity Type

General manufacturing & Custom automotive parts

Coding

Coded - Design and coding required

Number of Pages Required

5+ page

Requirements
Must have
• Automatic 3d print quoting. Shop for my printed parts.

```html
<!DOCTYPE html>
<html lang="en">
<head>
<meta charset="utf-8">
<title>KVR Draft &amp; Design</title>
<link href="https://fonts.googleapis.com/css2?family=Krona+One&family=Montserrat:wght@400;500;600;700;800&display=swap" rel="stylesheet">
<style>
:root{
  --orange:#f47b16;
  --orange-dark:#d9630a;
  --black:#000;
  --panel:#141210;
  --panel-2:#1d1a17;
  --white:#fff;
  --muted:#cfcfcf;
  --card-edge:#3a2a1c;
}
*{margin:0;padding:0;box-sizing:border-box}
html,body{width:1200px;height:4096px;overflow:hidden;background:var(--black);color:var(--white);font-family:'Montserrat',sans-serif}
.canvas{position:relative;width:1200px;height:4096px;overflow:hidden;background:var(--black)}
.abs{position:absolute}
.display{font-family:'Krona One',sans-serif;font-weight:400}
.btn{position:absolute;display:flex;align-items:center;justify-content:center;background:var(--orange);color:var(--white);font-weight:700;font-size:15px;letter-spacing:.3px;transform:skewX(-18deg);box-shadow:5px 4px 0 var(--orange-dark)}
.btn span{transform:skewX(18deg)}
.photo{position:absolute}

/* header */
.header{position:absolute;left:0;top:0;width:1200px;height:124px;background:var(--black);border-bottom:2px solid var(--orange-dark)}
.brand{position:absolute;display:flex;align-items:center;gap:10px;color:var(--orange);font-weight:800}
.brand .dot{width:14px;height:14px;border-radius:50%;background:var(--orange)}
.contact-chip{position:absolute;display:flex;align-items:center;gap:10px;top:12px}
.contact-chip .ico{width:40px;height:40px;border-radius:50%;background:var(--orange);display:flex;align-items:center;justify-content:center}
.contact-chip small{display:block;font-size:12px;font-weight:600}
.contact-chip b{display:block;font-size:16px;font-weight:600}
.nav{position:absolute;top:78px;font-size:15px;font-weight:600;letter-spacing:.3px}
.nav.active{color:var(--orange);border-bottom:2px solid var(--orange);padding-bottom:6px}

/* hero */
.hero-photo{left:0;top:124px;width:1200px;height:663px;background:
 radial-gradient(ellipse at 62% 55%,rgba(250,220,40,.9) 0%,rgba(240,120,30,.6) 18%,transparent 38%),
 radial-gradient(ellipse at 78% 25%,rgba(220,60,150,.7) 0%,transparent 35%),
 radial-gradient(ellipse at 35% 30%,rgba(60,160,200,.6) 0%,transparent 40%),
 linear-gradient(120deg,#1c2a3a 0%,#3b3f52 40%,#5a3a60 65%,#2a2030 100%)}
.hero-title{left:100px;top:288px;font-size:57px;line-height:56px;color:var(--white)}
.hero-text{left:101px;top:410px;width:460px;font-size:17px;line-height:27px;font-weight:500}
.dots{left:560px;top:708px;display:flex;gap:9px}
.dots i{width:14px;height:14px;border-radius:50%;background:#ddd;display:block}
.dots i:first-child{background:transparent;border:2px solid #fff}

/* about */
.about-bg-word{left:-6px;top:1230px;transform:rotate(-90deg);transform-origin:left top;font-size:70px;color:#2a2a2a}
.about-photo{left:105px;top:837px;width:462px;height:344px;background:linear-gradient(135deg,#2f5670,#1a2a36 50%,#54636b)}
.section-title{font-size:40px;line-height:44px;letter-spacing:1px}
.about-text{left:642px;top:922px;width:460px;font-size:13.5px;line-height:23px;color:var(--muted)}
.about-text p+p{margin-top:10px}

/* service cards */
.svc-photo{top:1260px;height:512px}
.svc-caption{position:absolute;top:1602px;width:467px;height:135px;background:rgba(240,240,240,.92);color:#222;text-align:center;padding-top:22px}
.svc-caption h3{font-family:'Krona One',sans-serif;font-size:22px;font-weight:400;color:#111}
.svc-caption p{font-size:13px;line-height:22px;color:#444;margin:8px 24px 0}

/* products */
.product{position:absolute;top:1932px;width:237px;height:272px;background:#1d1a17;border:2px solid var(--card-edge);text-align:center}
.product .pimg{height:186px;margin:3px;background:linear-gradient(160deg,#9a5c33,#5a3319)}
.product h4{font-size:16px;font-weight:600;margin-top:14px}
.product .price{color:var(--orange);font-size:14px;margin-top:4px}
.product .stars{color:var(--orange);font-size:13px;letter-spacing:1px}

/* services list */
.services{left:0;top:2285px;width:1200px;height:531px;background:linear-gradient(90deg,#0d0c0b,#25211d 60%,#1a1714)}
.svc-item{position:absolute;display:flex;align-items:center;gap:10px;font-family:'Krona One',sans-serif;font-size:15px}
.tick{width:24px;height:24px}

/* blog */
.blog{position:absolute;top:2963px;width:318px;height:414px;background:#141210;border:2px solid var(--card-edge);padding:10px}
.blog .bimg{height:203px;background:linear-gradient(150deg,#6b6b6b,#2b2b2b)}
.blog h4{font-size:20px;font-weight:600;line-height:26px;margin:14px 0 0 6px}
.blog p{font-size:13.5px;line-height:26px;color:var(--muted);margin:6px 8px 0 8px}
.blog a{display:block;color:var(--orange);font-weight:700;font-size:14px;text-decoration:underline;margin:8px 0 0 14px}

/* footer */
.foot-head{font-size:17px;font-weight:600}
.foot-list{font-size:13px;line-height:32.5px;color:var(--muted)}
.social{position:absolute;top:3993px;width:28px;height:28px;border:1.5px solid #fff;border-radius:50%}
.pay{position:absolute;top:3950px;width:52px;height:32px;border-radius:3px}
</style>
</head>
<body>
<div class="canvas">

  <!-- header -->
  <header class="header">
    <div class="brand" style="left:99px;top:30px;font-size:24px;line-height:28px">
      <span class="dot"></span><span>KVR<br><span style="font-size:15px">Draft &amp; Design</span></span>
    </div>
    <div class="contact-chip" style="left:505px">
      <span class="ico"><svg width="20" height="20" viewBox="0 0 24 24"><path fill="#fff" d="M6.6 10.8a15 15 0 0 0 6.6 6.6l2.2-2.2c.3-.3.7-.4 1-.2 1.1.4 2.3.6 3.6.6.6 0 1 .4 1 1V20c0 .6-.4 1-1 1A17 17 0 0 1 3 4c0-.6.4-1 1-1h3.5c.6 0 1 .4 1 1 0 1.3.2 2.5.6 3.6.1.3 0 .7-.2 1z"/></svg></span>
      <span><small>CALL US</small><b>+61 400 718 205</b></span>
    </div>
    <div class="contact-chip" style="left:696px">
      <span class="ico"><svg width="20" height="16" viewBox="0 0 24 18"><rect x="1" y="1" width="22" height="16" rx="2" fill="#fff"/><path d="M2 2l10 8 10-8" stroke="#f47b16" stroke-width="2" fill="none"/></svg></span>
      <span><small>EMAIL</small><b>hello@kvrdraftdesign.com.au</b></span>
    </div>
    <div class="abs" style="left:1016px;top:14px;width:1px;height:38px;background:#555"></div>
    <svg class="abs" style="left:1034px;top:16px" width="24" height="26" viewBox="0 0 24 26"><circle cx="12" cy="8" r="6" stroke="#fff" stroke-width="1.6" fill="none"/><path d="M2 25c0-6 4.5-9 10-9s10 3 10 9" stroke="#fff" stroke-width="1.6" fill="none"/></svg>
    <svg class="abs" style="left:1068px;top:18px" width="30" height="24" viewBox="0 0 30 24"><path d="M2 8h22l-3 14H5z" stroke="#fff" stroke-width="1.6" fill="none"/><path d="M8 8l4-6M18 8l-4-6" stroke="#fff" stroke-width="1.6"/><circle cx="24" cy="6" r="5" fill="#f47b16"/></svg>
    <span class="nav active" style="left:318px">HOME</span>
    <span class="nav" style="left:400px">TECHNOLOGY</span>
    <span class="nav" style="left:543px">MATERIAL</span>
    <span class="nav" style="left:656px">PORTFOLIO</span>
    <span class="nav" style="left:782px">CONTACT US</span>
    <div class="btn" style="left:906px;top:68px;width:186px;height:40px"><span>INSTANT QUOTE »</span></div>
  </header>

  <!-- hero -->
  <div class="photo hero-photo" role="img" aria-label="Close-up of a 3D printer nozzle extruding filament in colourful light"></div>
  <svg class="abs" style="left:64px;top:428px" width="20" height="36" viewBox="0 0 20 36"><path d="M18 2L3 18l15 16" stroke="#fff" stroke-width="2" fill="none"/></svg>
  <h1 class="abs display hero-title">KVR DRAFT<br>&amp; DESIGN</h1>
  <p class="abs hero-text">Lorem ipsum dolor sit amet, constetur adipiscing elit, sed do eiusmod tempor</p>
  <div class="btn" style="left:105px;top:488px;width:224px;height:36px"><span>UPLOAD A 3D MODEL »</span></div>
  <div class="abs dots"><i></i><i></i><i></i><i></i></div>
  <svg class="abs" style="left:0;top:720px" width="1200" height="70" viewBox="0 0 1200 70" preserveAspectRatio="none">
    <path d="M0 66 L160 12 L420 38 L600 52 L780 38 L1010 14 L1200 66 Z" fill="var(--orange)"/>
    <path d="M0 70 L160 24 L420 48 L600 62 L780 48 L1010 26 L1200 70 Z" fill="var(--black)"/>
  </svg>

  <!-- about -->
  <div class="abs display about-bg-word">ABOUT US</div>
  <svg class="abs" style="left:96px;top:828px" width="480" height="362" viewBox="0 0 480 362">
    <path d="M280 3H477V170" stroke="#f47b16" stroke-width="5" fill="none"/>
    <path d="M3 290V359H198" stroke="#f47b16" stroke-width="5" fill="none"/>
  </svg>
  <div class="photo about-photo" role="img" aria-label="Engineer working at a laptop beside a 3D printer in a workshop"></div>
  <h2 class="abs display section-title" style="left:637px;top:852px">ABOUT US</h2>
  <div class="abs about-text">
    <p>Lorem ipsum dolor sit amet, consectetur adipiscingid do eiusmod tempor incididunt ut labore et dolore ma. Quis ipsum suspendisse ultrices gravida. Risus commodo viverra maejnas accumsan lacus vel facilisis.</p>
    <p>Lorem ipsum dolor sit amet, consectetur adipiscingid do eiusmod tempor incididunt ut labore et dolore ma. Quis ipsum suspendisse ultrices gravida</p>
  </div>
  <div class="btn" style="left:645px;top:1116px;width:162px;height:38px"><span>READ MORE »</span></div>

  <!-- technology cards -->
  <div class="photo svc-photo" style="left:0;width:599px;background:linear-gradient(150deg,#3a3a3a,#1a1a1a 50%,#1d7a82 75%,#2a2a2a)" role="img" aria-label="SLA resin printer producing a teal gear part"></div>
  <div class="abs" style="left:599px;top:1260px;width:4px;height:512px;background:#fff"></div>
  <div class="photo svc-photo" style="left:603px;width:597px;background:linear-gradient(160deg,#4a4a4a,#222 45%,#2a3d6e 85%)" role="img" aria-label="FDM printer head with cooling fan above a blue bed"></div>
  <div class="svc-caption" style="left:67px"><h3>SLA 3D Printing service</h3><p>Lorem ipsum dolor sit amet, consectetur adipiscingid do eiusmod tempor incididunt ut labore et dolore ma</p></div>
  <div class="btn" style="left:220px;top:1716px;width:156px;height:36px"><span>READ MORE »</span></div>
  <div class="svc-caption" style="left:666px"><h3>FDM 3D Printing service</h3><p>Lorem ipsum dolor sit amet, consectetur adipiscingid do eiusmod tempor incididunt ut labore et dolore ma</p></div>
  <div class="btn" style="left:820px;top:1716px;width:156px;height:36px"><span>READ MORE »</span></div>

  <!-- featured products -->
  <h2 class="abs display section-title" style="left:0;width:1200px;text-align:center;top:1850px">FEATURED PRODUCTS</h2>
  <div class="abs" style="left:572px;top:1902px;width:60px;height:3px;background:var(--orange)"></div>
  <div class="product" style="left:99px"><div class="pimg" role="img" aria-label="Grey printed automotive bracket on wood"></div><h4>Finibus Boum Malorum</h4><div class="price">$00.00</div><div class="stars">★★★★★</div></div>
  <div class="product" style="left:352px"><div class="pimg" role="img" aria-label="Flat printed mounting plate on wood"></div><h4>Finibus Boum Malorum</h4><div class="price">$00.00</div><div class="stars">★★★★★</div></div>
  <div class="product" style="left:606px"><div class="pimg" role="img" aria-label="White printed pipe adapter on wood"></div><h4>Finibus Boum Malorum</h4><div class="price">$00.00</div><div class="stars">★★★★★</div></div>
  <div class="product" style="left:860px"><div class="pimg" role="img" aria-label="White printed duct housing on wood"></div><h4>Finibus Boum Malorum</h4><div class="price">$00.00</div><div class="stars">★★★★★</div></div>

  <!-- our services -->
  <div class="abs services"></div>
  <h2 class="abs display section-title" style="left:99px;top:2364px">OUR SERIVES</h2>
  <p class="abs" style="left:99px;top:2426px;width:480px;font-size:13.5px;line-height:24px;color:var(--muted)">Lorem ipsum dolor sit amet, consectetur adipiscingid do eiusmod tempor incididunt ut labore et dolore ma.</p>
  <div class="svc-item" style="left:99px;top:2505px"><svg class="tick" viewBox="0 0 24 24"><circle cx="12" cy="12" r="10" stroke="#f47b16" stroke-width="2" fill="none"/><path d="M7 12l4 4 9-10" stroke="#f47b16" stroke-width="2.4" fill="none"/></svg>3d printing</div>
  <div class="svc-item" style="left:342px;top:2505px"><svg class="tick" viewBox="0 0 24 24"><circle cx="12" cy="12" r="10" stroke="#f47b16" stroke-width="2" fill="none"/><path d="M7 12l4 4 9-10" stroke="#f47b16" stroke-width="2.4" fill="none"/></svg>3d scanning</div>
  <div class="svc-item" style="left:99px;top:2561px"><svg class="tick" viewBox="0 0 24 24"><circle cx="12" cy="12" r="10" stroke="#f47b16" stroke-width="2" fill="none"/><path d="M7 12l4 4 9-10" stroke="#f47b16" stroke-width="2.4" fill="none"/></svg>3d Cad Design</div>
  <div class="svc-item" style="left:342px;top:2561px"><svg class="tick" viewBox="0 0 24 24"><circle cx="12" cy="12" r="10" stroke="#f47b16" stroke-width="2" fill="none"/><path d="M7 12l4 4 9-10" stroke="#f47b16" stroke-width="2.4" fill="none"/></svg>Cnc Machining</div>
  <div class="svc-item" style="left:99px;top:2624px"><svg class="tick" viewBox="0 0 24 24"><circle cx="12" cy="12" r="10" stroke="#f47b16" stroke-width="2" fill="none"/><path d="M7 12l4 4 9-10" stroke="#f47b16" stroke-width="2.4" fill="none"/></svg>Steel Fabrication</div>
  <div class="svc-item" style="left:342px;top:2624px"><svg class="tick" viewBox="0 0 24 24"><circle cx="12" cy="12" r="10" stroke="#f47b16" stroke-width="2" fill="none"/><path d="M7 12l4 4 9-10" stroke="#f47b16" stroke-width="2.4" fill="none"/></svg>Drafting Services</div>
  <div class="btn" style="left:101px;top:2690px;width:166px;height:38px"><span>READ MORE »</span></div>
  <div class="photo" style="left:664px;top:2360px;width:397px;height:376px;background:radial-gradient(circle at 58% 55%,#8fbf2a 0%,#3a3a3a 22%,#1c1c1c 60%,transparent 75%)" role="img" aria-label="Compact desktop 3D printer with enclosure"></div>

  <!-- blog -->
  <h2 class="abs display section-title" style="left:0;width:1200px;text-align:center;top:2888px">LATEST BLOG</h2>
  <article class="blog" style="left:99px"><div class="bimg" role="img" aria-label="Printed pump assembly in a workshop"></div><h4>The standard Lorem Ipsum passage, us the 1500s</h4><p>Lorem ipsum et, consectetur adipiscing elit, sed do eiusmod tempor incididunt ut labore et dolore magna aliqua.</p><a>READ MORE »</a></article>
  <article class="blog" style="left:440px"><div class="bimg" style="background:linear-gradient(150deg,#888,#3d3d3d)" role="img" aria-label="Printed dashboard gauge cluster on fur"></div><h4>The standard Lorem Ipsum passage, us the 1500s</h4><p>Lorem ipsum et, consectetur adipiscing elit, sed do eiusmod tempor incididunt ut labore et dolore magna aliqua.</p><a>READ MORE »</a></article>
  <article class="blog" style="left:782px"><div class="bimg" style="background:linear-gradient(150deg,#7a6a55,#c9a040 55%,#3a3a3a)" role="img" aria-label="Assorted printed parts on a table"></div><h4>The standard Lorem Ipsum passage, us the 1500s</h4><p>Lorem ipsum et, consectetur adipiscing elit, sed do eiusmod tempor incididunt ut labore et dolore magna aliqua.</p><a>READ MORE »</a></article>

  <!-- newsletter -->
  <svg class="abs" style="left:0;top:3420px" width="1200" height="80" viewBox="0 0 1200 80" preserveAspectRatio="none">
    <path d="M0 0 L240 62 L600 38 L960 62 L1200 0 L1200 14 L960 76 L600 52 L240 76 L0 14 Z" fill="var(--orange)"/>
  </svg>
  <p class="abs" style="left:0;width:1200px;text-align:center;top:3530px;font-size:14px;letter-spacing:4px;color:#ddd">OUR NEWSLETTER</p>
  <h3 class="abs display" style="left:0;width:1200px;text-align:center;top:3564px;font-size:26px;line-height:32px">Sign Up For Our Newsletter</h3>
  <p class="abs" style="left:0;width:1200px;text-align:center;top:3610px;font-size:14px;font-weight:600">Sign up to get the latest on sales new releases and more</p>
  <div class="abs" style="left:296px;top:3655px;width:608px;height:46px;background:#fff;border:2px solid var(--orange-dark);color:#333;font-size:14px;padding:13px 20px">Email Address</div>
  <div class="abs" style="left:760px;top:3657px;width:142px;height:42px;background:var(--orange);display:flex;align-items:center;justify-content:center;font-weight:700;font-size:15px">SUBMIT »</div>

  <!-- footer -->
  <div class="abs" style="left:99px;top:3766px;width:1001px;height:1px;background:#555"></div>
  <div class="brand" style="left:99px;top:3860px;font-size:44px;line-height:46px">
    <span class="dot" style="width:20px;height:20px"></span><span>KVR<br><span style="font-size:22px">Draft &amp; Design</span></span>
  </div>
  <span class="social" style="left:138px"></span>
  <span class="social" style="left:177px"></span>
  <span class="social" style="left:216px"></span>
  <span class="social" style="left:255px"></span>

  <h4 class="abs foot-head" style="left:432px;top:3812px">Quick Links</h4>
  <div class="abs foot-list" style="left:433px;top:3837px">Home<br>Technology<br>Material<br>Portfolio<br>Contact Us</div>
  <h4 class="abs foot-head" style="left:607px;top:3812px">Contact Info</h4>
  <div class="abs" style="left:608px;top:3842px;font-size:13px;line-height:23px;color:var(--muted)">1234 Main Rd<br>Somewhere, US 12345</div>
  <div class="abs" style="left:608px;top:3898px;font-size:13px;color:var(--muted)">+61 400 718 205</div>
  <div class="abs" style="left:608px;top:3931px;font-size:13px;color:var(--muted)">hello@kvrdraftdesign.com.au</div>
  <h4 class="abs foot-head" style="left:863px;top:3812px">Connect</h4>
  <div class="abs" style="left:864px;top:3842px;width:240px;font-size:13px;line-height:26px;color:var(--muted)">Customer Service<br>We're here to help! Our Customer services Team is here to assist you</div>
  <span class="pay" style="left:866px;background:#e8eef5"></span>
  <span class="pay" style="left:925px;background:#3a3a3a"></span>
  <span class="pay" style="left:984px;background:#e8eef5"></span>
  <span class="pay" style="left:1043px;background:#2f7cc0"></span>

  <div class="abs" style="left:99px;top:4036px;width:1001px;height:1px;background:#555"></div>
  <p class="abs" style="left:0;width:1200px;text-align:center;top:4055px;font-size:13px;color:var(--muted)">©Copyright ©2023 KVR Draft &amp; Design&nbsp; All Rights Reserved.</p>
</div>
</body>
</html>
```